Increasing performance of Security Operations Centers

Stellavant builds Security Operations Centers (SOC) that enable Pinnacle 1000 clients to be proactive and predictive in the way they secure their people and facilities. The methods involve automating threat detection, streamlining workflows, and outsourcing the most appropriate tasks. The outcomes are a reduction in total incidents and faster response times with fewer resources so clients can focus on their core business.
We're looking for 2 slides to replace the attached PPT. The first slide would be broken into each of the 8 capabilities when presenting: i.e. starting with "Reduce incidents..." on the first slide, building on with "Better direct..." on the second and continuing around clockwise. I'm looking for a more compelling way to present the capabilities and am not wedded to the way it is laid out now.
Also attached is our brand book for color and font values to comply with.

I will extend the deadline to 3/28 as soon as I figure out how.

```html
<!DOCTYPE html>
<html lang="en">
<head>
<meta charset="utf-8">
<title>SOC Performance Improvement Objectives</title>
<link href="https://fonts.googleapis.com/css2?family=Inter:wght@300;400;600;700&display=swap" rel="stylesheet">
<style>
:root{
  --navy:#0c2c4a;
  --red:#c42d2a;
  --ink:#222831;
  --text:#2f3540;
  --halo-red:#e6c3c4;
  --halo-blue:#c6d6e6;
  --core:#e9f0f5;
  --line:#d4dbe2;
  --page:#ffffff;
}
*{margin:0;padding:0;box-sizing:border-box}
html,body{width:1042px;height:1200px;overflow:hidden;background:var(--page);font-family:"Inter",Helvetica,Arial,sans-serif}
.canvas{position:relative;width:1042px;height:1200px}
.slide{position:absolute;left:29px;width:984px;height:553px;overflow:hidden;
  background:linear-gradient(120deg,#e8eef3 0%,#f6f8fa 45%,#fbfcfd 70%,#f1f4f7 100%)}
.slide--one{top:31px}
.slide--two{top:604px}
.art{position:absolute;left:0;top:0}
.slide-title{position:absolute;left:27px;top:19px;font-size:25px;font-weight:700;color:var(--ink);letter-spacing:-.3px}
.brand{position:absolute;right:28px;top:10px;font-size:30px;font-weight:400;color:#fff;letter-spacing:-.5px}
.page-no{position:absolute;left:962px;top:538px;font-size:9px;color:var(--ink)}
.label{position:absolute;font-size:14.5px;font-weight:300;color:var(--text);line-height:20.5px;letter-spacing:-.15px;white-space:nowrap}
.label--r{text-align:right}
.core-title{position:absolute;left:376px;top:285px;width:200px;text-align:center;font-size:18.5px;font-weight:600;color:var(--ink);line-height:26px}
.pillar{position:absolute;width:240px;text-align:center;font-size:20.5px;font-weight:300;color:var(--text);line-height:26px}
.tri-text{position:absolute;left:391px;top:289px;width:200px;text-align:center;font-size:18px;font-weight:700;color:var(--ink);line-height:26.5px;letter-spacing:-.2px}
.modes{position:absolute;left:0;top:473px;width:984px;display:flex;justify-content:center;gap:28px;align-items:center;font-size:20.5px;font-weight:600;color:var(--ink);line-height:26px}
.modes .dot{width:7px;height:7px;border-radius:50%;background:var(--red)}
</style>
</head>
<body>
<div class="canvas">

  <section class="slide slide--one">
    <svg class="art" width="984" height="553" viewBox="0 0 984 553" fill="none">
      <rect x="0" y="0" width="540" height="7" fill="var(--red)"/>
      <polygon points="538,0 984,0 984,56 582,56" fill="var(--navy)"/>
      <rect x="0" y="544" width="956" height="9" fill="var(--navy)"/>
      <polygon points="928,544 945,544 953,553 934,553" fill="var(--red)"/>
      <polygon points="479,148 596,196 644,317 595,434 475,482 357,434 309,317 358,196" stroke="var(--line)" stroke-width="1.5"/>
      <polygon points="479,165 585,208 626,317 584,423 475,466 368,423 327,317 369,208" fill="var(--core)"/>
      <polygon points="479,194 564,231 598,317 563,402 475,437 389,402 355,317 390,231" stroke="var(--line)" stroke-width="1"/>
      <g stroke-width="1.6">
        <circle cx="413" cy="157" r="36" fill="var(--halo-red)"/><circle cx="413" cy="157" r="29" fill="#fff" stroke="var(--navy)"/>
        <circle cx="328" cy="256" r="36" fill="var(--halo-red)"/><circle cx="328" cy="256" r="29" fill="#fff" stroke="var(--navy)"/>
        <circle cx="322" cy="376" r="36" fill="var(--halo-red)"/><circle cx="322" cy="376" r="29" fill="#fff" stroke="var(--navy)"/>
        <circle cx="405" cy="467" r="36" fill="var(--halo-red)"/><circle cx="405" cy="467" r="29" fill="#fff" stroke="var(--navy)"/>
        <circle cx="541" cy="157" r="36" fill="var(--halo-blue)"/><circle cx="541" cy="157" r="29" fill="#fff" stroke="var(--navy)"/>
        <circle cx="626" cy="256" r="36" fill="var(--halo-blue)"/><circle cx="626" cy="256" r="29" fill="#fff" stroke="var(--navy)"/>
        <circle cx="632" cy="376" r="36" fill="var(--halo-blue)"/><circle cx="632" cy="376" r="29" fill="#fff" stroke="var(--navy)"/>
        <circle cx="539" cy="467" r="36" fill="var(--halo-blue)"/><circle cx="539" cy="467" r="29" fill="#fff" stroke="var(--navy)"/>
      </g>
      <g stroke="var(--red)" stroke-width="1.4" stroke-linecap="round">
        <circle cx="413" cy="150" r="8"/><path d="M413 145v10M403 160v10l-3-3M403 170l3-3M413 160v12l-3-3M413 172l3-3M423 160v10l-3-3M423 170l3-3"/>
        <rect x="318" y="244" width="20" height="12" rx="2"/><circle cx="313" cy="262" r="5"/><circle cx="343" cy="262" r="5"/><path d="M322 270h12"/>
        <rect x="310" y="362" width="24" height="26" rx="2"/><path d="M310 368h24M322 372v8M316 380l6-6 6 6"/>
        <circle cx="401" cy="472" r="9"/><path d="M405 463l4-6M412 455l3-2"/>
      </g>
      <g stroke="var(--navy)" stroke-width="1.4" stroke-linecap="round">
        <circle cx="531" cy="147" r="5"/><circle cx="551" cy="147" r="5"/><circle cx="531" cy="167" r="5"/><circle cx="551" cy="167" r="5"/><circle cx="541" cy="157" r="4"/><path d="M536 147h10M536 167h10"/>
        <path d="M626 242l12 5v8c0 8-6 13-12 15-6-2-12-7-12-15v-8z"/><rect x="621" y="254" width="10" height="8" rx="1"/>
        <circle cx="637" cy="371" r="9"/><path d="M631 378l-12 12"/>
        <circle cx="539" cy="458" r="6"/><circle cx="530" cy="466" r="4"/><circle cx="548" cy="466" r="4"/><path d="M528 480v-6h22v6M534 480v-4h10v4"/>
      </g>
    </svg>
    <h1 class="slide-title">SOC Performance Improvement Objectives…</h1>
    <div class="brand">Stellavant</div>

    <div class="label label--r" style="right:624px;top:146px">Reduce Total Cost</div>
    <div class="label" style="left:598px;top:133px">Reduce incidents, respond faster,<br>with fewer resources</div>
    <div class="label label--r" style="right:704px;top:235px">Outsource Key or Non-Core<br>Functions</div>
    <div class="label" style="left:683px;top:224px">Better direct your security/safety<br>personnel to situations where they<br>are needed most.</div>
    <div class="label label--r" style="right:715px;top:356px">Automate threat detection,<br>streamline workflows,</div>
    <div class="label" style="left:689px;top:356px">Free up time for more engagement,<br>deterrence, and investigations.</div>
    <div class="label label--r" style="right:633px;top:446px">Increase your installed systems<br>protective usefulness &amp; adaptability<br>to new threats</div>
    <div class="label" style="left:595px;top:456px">Lessen your management burden.</div>

    <div class="core-title">SOC<br>Performance</div>
    <div class="page-no">01</div>
  </section>

  <section class="slide slide--two">
    <svg class="art" width="984" height="553" viewBox="0 0 984 553" fill="none">
      <rect x="0" y="0" width="540" height="7" fill="var(--red)"/>
      <polygon points="538,0 984,0 984,56 582,56" fill="var(--navy)"/>
      <rect x="0" y="544" width="956" height="9" fill="var(--navy)"/>
      <polygon points="928,544 945,544 953,553 934,553" fill="var(--red)"/>
      <path d="M479 226 Q491 203 503 226 L595 383 Q603 398 585 398 L397 398 Q379 398 387 383 Z" fill="#eef3f7" stroke="var(--navy)" stroke-width="13" stroke-linejoin="round"/>
      <g stroke-width="1.5" stroke-linecap="round">
        <rect x="466" y="102" width="25" height="18" rx="2" stroke="var(--navy)"/>
        <path d="M470 124h10M466 130h12M468 136h10" stroke="var(--red)"/>
        <circle cx="501" cy="134" r="15" stroke="var(--red)"/><path d="M501 126v9M497 117h8" stroke="var(--navy)"/>
      </g>
      <g stroke-width="1.5" stroke-linecap="round" stroke-linejoin="round">
        <path d="M250 395l-12-2 16-28 16 28z" stroke="var(--red)"/>
        <path d="M254 375v10M254 390v1" stroke="var(--red)"/>
        <path d="M242 338v12l-4-4M242 350l4-4M262 338v12l-4-4M262 350l4-4M228 352v14l-4-4M228 366l4-4M272 352v14l-4-4M272 366l4-4" stroke="var(--navy)"/>
      </g>
      <g stroke-width="1.5" stroke-linecap="round" stroke-linejoin="round">
        <circle cx="727" cy="347" r="7" stroke="var(--navy)"/>
        <circle cx="714" cy="361" r="7" stroke="var(--red)"/><circle cx="740" cy="361" r="6" stroke="var(--red)"/>
        <path d="M706 372v12h14l22-8-4-3-14 4" stroke="var(--red)"/>
      </g>
    </svg>
    <h1 class="slide-title">SOC Performance Improvement Objectives…</h1>
    <div class="brand">Stellavant</div>

    <div class="pillar" style="left:371px;top:156px">Respond Faster</div>
    <div class="tri-text">Reduce<br>Total Cost of<br>Operations</div>
    <div class="pillar" style="left:131px;top:397px">Reduce&nbsp; Incidents</div>
    <div class="pillar" style="left:607px;top:397px">Fewer Resources</div>

    <div class="modes"><span>Proactive</span><span class="dot"></span><span>Predictive</span><span class="dot"></span><span>Preventative</span></div>
    <div class="page-no">02</div>
  </section>

</div>
</body>
</html>
```